Electrical Services Flyer

We need to create a flyer which will be posted out across Melbourne to businesses to promote our new Electrical Services Division. Services we deliver include but are not limited to - Office Shop fit outs- Lighting and Lighting Automation - Exit and Emergency lighting - Body Corporate works- Thermal Imaging- Test and Tagging- Fault Diagnosis- Switchboard Maintenance/UpgradesFor more on our company please visit corvelmapower.com.au

Target Market(s)

Businesses

Colors

Designer to choose colors to be used in the design.

Requirements
Must have
• A modern look, simple clean eye catching.
• A clear way to contact the business
• 148 272
• Quote@corvelma.com.au
Nice to have
• A simple eye catching design that attracts the eye with a simple catchy line like "need an electrician?"

```html
<!DOCTYPE html>
<html lang="en">
<head>
<meta charset="utf-8">
<title>Corvelma Electrical Services – Need an Electrician?</title>
<link href="https://fonts.googleapis.com/css2?family=Oswald:wght@400;500;600&display=swap" rel="stylesheet">
<style>
  :root{
    --blue:#3450a7;
    --blue-deep:#2b4399;
    --orange:#f26f21;
    --orange-2:#f7884a;
    --orange-3:#f9a472;
    --orange-4:#fbc39f;
    --orange-5:#fde0cc;
    --grey:#e6e7ea;
    --grey-line:#d9dbe0;
    --white:#ffffff;
  }
  html,body{margin:0;padding:0;width:1104px;height:1200px;overflow:hidden;background:var(--white);}
  .flyer{position:relative;width:1104px;height:1200px;font-family:"Oswald",sans-serif;overflow:hidden;}
  .flyer-shapes{position:absolute;left:0;top:0;}
  .brand{position:absolute;left:47px;top:47px;display:flex;align-items:center;gap:16px;color:var(--blue-deep);font-weight:600;}
  .brand-dot{width:86px;height:86px;border-radius:50%;background:var(--orange);}
  .brand-name{line-height:1;}
  .brand-name .main{display:block;font-size:56px;letter-spacing:-0.5px;}
  .brand-name .sub{display:block;font-size:20px;letter-spacing:2.4px;margin-top:4px;}
  .tagline{position:absolute;left:600px;top:72px;width:488px;margin:0;text-align:right;font-size:28px;line-height:40px;font-weight:400;color:var(--blue);letter-spacing:0.2px;}
  .headline{position:absolute;left:50px;top:340px;margin:0;color:var(--white);font-weight:500;font-size:84px;line-height:92px;letter-spacing:0.5px;}
  .services-title{position:absolute;left:286px;top:784px;width:531px;text-align:center;margin:0;font-size:42px;font-weight:500;color:var(--blue);line-height:52px;}
  .service-list{position:absolute;top:870px;margin:0;padding:0;list-style:none;}
  .service-list.left{left:67px;}
  .service-list.right{left:692px;}
  .service-list li{display:flex;align-items:center;gap:16px;height:50.4px;font-size:31px;font-weight:500;color:var(--orange);}
  .service-list svg{flex:none;}
  .contact-label{position:absolute;left:62px;top:1107px;font-size:54px;font-weight:500;color:var(--white);line-height:70px;}
  .phone{position:absolute;left:366px;top:1098px;display:flex;align-items:center;gap:16px;color:var(--white);}
  .phone-number{font-size:78px;font-weight:500;line-height:90px;letter-spacing:1px;}
  .contact-divider{position:absolute;left:705px;top:1114px;width:1px;height:62px;background:rgba(255,255,255,.55);}
  .contact-links{position:absolute;left:739px;top:1115px;color:var(--white);font-size:21px;font-weight:400;line-height:30px;}
  .contact-links div{display:flex;align-items:center;gap:11px;}
</style>
</head>
<body>
<main class="flyer">
  <svg class="flyer-shapes" width="1104" height="1200" viewBox="0 0 1104 1200">
    <defs>
      <linearGradient id="g-team" x1="0" y1="0" x2="1" y2="1">
        <stop offset="0" stop-color="#c9ccd0"/><stop offset=".5" stop-color="#9aa0a8"/><stop offset="1" stop-color="#6f7a86"/>
      </linearGradient>
      <linearGradient id="g-hall" x1="0" y1="0" x2="0" y2="1">
        <stop offset="0" stop-color="#e9e3dc"/><stop offset=".5" stop-color="#a83a2c"/><stop offset="1" stop-color="#3a3d42"/>
      </linearGradient>
      <linearGradient id="g-lounge" x1="0" y1="0" x2="0" y2="1">
        <stop offset="0" stop-color="#cfc7ba"/><stop offset="1" stop-color="#8f8c86"/>
      </linearGradient>
      <linearGradient id="g-church" x1="0" y1="0" x2="0" y2="1">
        <stop offset="0" stop-color="#b0713f"/><stop offset=".6" stop-color="#e4c7a3"/><stop offset="1" stop-color="#8a5a36"/>
      </linearGradient>
    </defs>

    <!-- top right stripe band -->
    <rect x="890" y="0" width="214" height="58" fill="var(--grey)"/>
    <polygon points="770,0 795,0 780,58 755,58" fill="var(--orange)"/>
    <polygon points="818,0 843,0 828,58 803,58" fill="var(--orange-2)"/>
    <polygon points="866,0 891,0 876,58 851,58" fill="var(--orange-3)"/>
    <polygon points="914,0 939,0 924,58 899,58" fill="var(--orange-4)"/>
    <polygon points="962,0 987,0 972,58 947,58" fill="var(--orange-5)"/>

    <!-- tagline plate -->
    <polygon points="592,61 1104,61 1104,123 555,123" fill="var(--white)" stroke="var(--grey-line)" stroke-width="3"/>
    <rect x="980" y="125" width="124" height="10" fill="var(--grey)"/>
    <rect x="738" y="125" width="24" height="10" fill="var(--orange)"/>
    <rect x="785" y="125" width="24" height="10" fill="var(--orange-2)"/>
    <rect x="832" y="125" width="24" height="10" fill="var(--orange-3)"/>
    <rect x="879" y="125" width="24" height="10" fill="var(--orange-4)"/>
    <rect x="926" y="125" width="24" height="10" fill="var(--orange-5)"/>

    <!-- hero -->
    <polygon class="hero-panel" points="0,199 414,199 318,292 650,562 0,562" fill="var(--blue)"/>
    <polygon role="img" aria-label="Photo: two electricians in hard hats and hi-vis vests inspecting cabling in a building"
      points="481,148 1104,148 1104,515 663,515 332,292" fill="url(#g-team)"/>

    <!-- hero bottom stripes -->
    <rect x="890" y="526" width="214" height="36" fill="var(--grey)"/>
    <polygon points="656,526 680,526 670,562 646,562" fill="var(--orange)"/>
    <polygon points="703,526 727,526 717,562 693,562" fill="var(--orange-2)"/>
    <polygon points="750,526 774,526 764,562 740,562" fill="var(--orange-3)"/>
    <polygon points="797,526 821,526 811,562 787,562" fill="var(--orange-4)"/>
    <polygon points="844,526 868,526 858,562 834,562" fill="var(--orange-5)"/>

    <!-- project photos -->
    <polygon role="img" aria-label="Photo: fitted-out hall with red feature wall and ceiling lights"
      points="0,580 401,580 355,759 0,759" fill="url(#g-hall)"/>
    <polygon role="img" aria-label="Photo: modern lounge interior with glass partitions and lighting"
      points="414,580 746,580 707,759 366,759" fill="url(#g-lounge)"/>
    <polygon role="img" aria-label="Photo: church interior with circular pendant lighting"
      points="759,580 1104,580 1104,759 720,759" fill="url(#g-church)"/>

    <!-- services heading band -->
    <rect x="0" y="779" width="1104" height="7" fill="var(--grey)"/>
    <path d="M286,779 L817,779 L805,831 Q802,841 792,841 L311,841 Q301,841 298,831 Z" fill="var(--grey)"/>

    <!-- footer -->
    <rect x="0" y="1083" width="1104" height="117" fill="var(--orange)"/>
    <path d="M405,1094 L1104,1094 L1104,1200 L266,1200 L365,1110 Q378,1094 405,1094 Z" fill="var(--blue)"/>
  </svg>

  <div class="brand">
    <span class="brand-dot"></span>
    <span class="brand-name"><span class="main">Corvelma</span><span class="sub">ELECTRICAL SERVICES</span></span>
  </div>

  <p class="tagline">Practical, Reliable &amp; Customer Focused</p>

  <h1 class="headline">NEED AN<br>ELECTRICIAN?</h1>

  <h2 class="services-title">Services We Deliver</h2>

  <ul class="service-list left">
    <li><svg width="24" height="22" viewBox="0 0 24 22"><rect x="1.5" y="5" width="15" height="15" fill="none" stroke="var(--blue)" stroke-width="2"/><path d="M5 12 L9 16 L22 2" fill="none" stroke="var(--orange)" stroke-width="2.5"/></svg>Office Shop fit outs</li>
    <li><svg width="24" height="22" viewBox="0 0 24 22"><rect x="1.5" y="5" width="15" height="15" fill="none" stroke="var(--blue)" stroke-width="2"/><path d="M5 12 L9 16 L22 2" fill="none" stroke="var(--orange)" stroke-width="2.5"/></svg>Lighting and Lighting Automation</li>
    <li><svg width="24" height="22" viewBox="0 0 24 22"><rect x="1.5" y="5" width="15" height="15" fill="none" stroke="var(--blue)" stroke-width="2"/><path d="M5 12 L9 16 L22 2" fill="none" stroke="var(--orange)" stroke-width="2.5"/></svg>Exit and Emergency lighting</li>
    <li><svg width="24" height="22" viewBox="0 0 24 22"><rect x="1.5" y="5" width="15" height="15" fill="none" stroke="var(--blue)" stroke-width="2"/><path d="M5 12 L9 16 L22 2" fill="none" stroke="var(--orange)" stroke-width="2.5"/></svg>Switchboard Maintenance/Upgrades</li>
  </ul>
  <ul class="service-list right">
    <li><svg width="24" height="22" viewBox="0 0 24 22"><rect x="1.5" y="5" width="15" height="15" fill="none" stroke="var(--blue)" stroke-width="2"/><path d="M5 12 L9 16 L22 2" fill="none" stroke="var(--orange)" stroke-width="2.5"/></svg>Body Corporate works</li>
    <li><svg width="24" height="22" viewBox="0 0 24 22"><rect x="1.5" y="5" width="15" height="15" fill="none" stroke="var(--blue)" stroke-width="2"/><path d="M5 12 L9 16 L22 2" fill="none" stroke="var(--orange)" stroke-width="2.5"/></svg>Thermal Imaging</li>
    <li><svg width="24" height="22" viewBox="0 0 24 22"><rect x="1.5" y="5" width="15" height="15" fill="none" stroke="var(--blue)" stroke-width="2"/><path d="M5 12 L9 16 L22 2" fill="none" stroke="var(--orange)" stroke-width="2.5"/></svg>Test and Tagging</li>
    <li><svg width="24" height="22" viewBox="0 0 24 22"><rect x="1.5" y="5" width="15" height="15" fill="none" stroke="var(--blue)" stroke-width="2"/><path d="M5 12 L9 16 L22 2" fill="none" stroke="var(--orange)" stroke-width="2.5"/></svg>Fault Diagnosis</li>
  </ul>

  <div class="contact-label">Contact</div>
  <div class="phone">
    <svg width="54" height="54" viewBox="0 0 24 24" aria-hidden="true"><path fill="var(--orange)" d="M6.6 10.8c1.4 2.8 3.8 5.1 6.6 6.6l2.2-2.2c.3-.3.7-.4 1-.2 1.1.4 2.3.6 3.6.6.6 0 1 .4 1 1V20c0 .6-.4 1-1 1C10.6 21 3 13.4 3 4c0-.6.4-1 1-1h3.5c.6 0 1 .4 1 1 0 1.3.2 2.5.6 3.6.1.3 0 .7-.2 1l-2.3 2.2z"/></svg>
    <span class="phone-number">148 272</span>
  </div>
  <div class="contact-divider"></div>
  <div class="contact-links">
    <div><svg width="18" height="13" viewBox="0 0 18 13" aria-hidden="true"><rect width="18" height="13" rx="1" fill="var(--orange)"/><path d="M1 1 L9 7 L17 1" fill="none" stroke="var(--blue)" stroke-width="1.5"/></svg>Quote@corvelma.com.au</div>
    <div><svg width="18" height="18" viewBox="0 0 18 18" aria-hidden="true"><circle cx="9" cy="9" r="8" fill="var(--orange)"/><path d="M1 9 H17 M9 1 V17 M9 1 C4 5 4 13 9 17 M9 1 C14 5 14 13 9 17" fill="none" stroke="var(--blue)" stroke-width="1.2"/></svg>www.corvelmapower.com.au</div>
  </div>
</main>
</body>
</html>
```